I need to redesign my landing page into a high converting landing page adding 3 new elements

I need to redesign my landing page using all the same content, images etc. on the current page https://www.brightlanepromoworks.biz/travel_agency but also adding three new elements to the new redesign.

Please be sure to use my current header and footer from my current website since I will just plug the new design into it...

The Three New Elements Are Below (add these 3 new elements in addition to the current content)

1. Add a video element with this content:
Watch Below To See How Your Industry Uses Our Incentives To Skyrocket Their Sales!

2. Add the element of the 6 types of incentives they can offer.
You can use the same content and images that we use in this module on the homepage at www.brightlanepromoworks.biz ATTACHED IMAGE BUT YOU CAN FIND THE ORIGINAL IMAGES ON HOMEPAGE

3. Add 1 more call to action to give website visitors two choices:
A. Sign Up For 14 Days Risk Free
OR
B. Book A Live Call

Target Market(s)

Travel agents and travel advisors

Industry/Entity Type

marketing

Requirements
Must have
• HIGH CONVERTING LANDING PAGE
Nice to have
• short and to the point...no fluff

```html
<!DOCTYPE html>
<html lang="en">
<head>
<meta charset="utf-8">
<title>Brightlane Promoworks – Travel Agency Incentives</title>
<link href="https://fonts.googleapis.com/css2?family=Poppins:wght@400;500;600;700;800&display=swap" rel="stylesheet">
<style>
:root{
  --navy:#1b1760;
  --navy-deep:#141046;
  --purple:#5a2fb0;
  --violet:#7b4fe0;
  --red:#e8442d;
  --green:#3cc24a;
  --yellow:#f6c21c;
  --ink:#1c1c2e;
  --muted:#5b5b70;
  --light:#f3f1fb;
  --white:#ffffff;
}
*{box-sizing:border-box;margin:0;padding:0}
html,body{width:1200px;height:4212px;overflow:hidden}
body{font-family:"Poppins",sans-serif;color:var(--ink);background:var(--white);position:relative}
section,header,footer{position:relative;width:1200px}
.btn{display:inline-block;font-weight:600;font-size:14px;padding:10px 22px;border-radius:22px;text-decoration:none}
.btn-red{background:var(--red);color:var(--white)}
.btn-outline{background:var(--white);color:var(--red);border:2px solid var(--red)}
.note{font-size:11px;color:var(--muted);margin-top:8px}
.center{text-align:center}

/* header */
.topbar{height:72px;display:flex;align-items:center;justify-content:space-between;padding:0 40px;background:var(--white)}
.brand{display:flex;align-items:center;gap:10px;font-weight:800;font-size:22px;color:var(--navy)}
.brand-dot{width:34px;height:34px;border-radius:50%;background:var(--purple)}
.brand small{display:block;font-size:10px;font-weight:600;letter-spacing:2px;color:var(--purple)}
.account{display:flex;gap:26px;font-size:14px;font-weight:600;color:var(--navy)}
.account span::before{content:"";display:inline-block;width:14px;height:14px;border-radius:50%;background:var(--purple);margin-right:6px;vertical-align:-2px}
.navbar{height:48px;background:var(--navy);display:flex;align-items:center;padding:0 40px;gap:30px;color:var(--white);font-size:13px;font-weight:500}
.navbar .spacer{flex:1}
.nav-btn{padding:7px 18px;border-radius:18px;font-weight:700;font-size:13px}
.nav-green{background:var(--green)}
.nav-yellow{background:var(--yellow);color:var(--navy)}

/* hero */
.hero{height:448px;background:linear-gradient(180deg,#eeebfa 0%,#ffffff 85%);text-align:center;padding-top:30px}
.hero h1{font-size:34px;font-weight:800;line-height:1.25;color:var(--navy)}
.hero h1 em{font-style:normal;color:var(--purple)}
.hero .lead{font-size:13px;margin:10px 0 12px;color:var(--ink)}
.hero .lead b{color:var(--purple)}
.video{width:340px;height:190px;margin:0 auto;border-radius:10px;background:linear-gradient(135deg,#2aa9c9,#1d6f8f 55%,#0d3a55);position:relative;border:4px solid var(--white);box-shadow:0 6px 18px rgba(27,23,96,.25)}
.video svg{position:absolute;left:50%;top:50%;transform:translate(-50%,-50%)}
.hero .ctas{margin-top:22px;display:flex;gap:16px;justify-content:center}

/* stats */
.stats{height:132px;background:var(--navy);display:flex;align-items:center;justify-content:space-around;padding:0 30px;color:var(--white)}
.stat{display:flex;align-items:center;gap:10px}
.stat-icon{width:40px;height:40px;border:2px solid #b9a8ff;border-radius:50%}
.stat b{display:block;font-size:24px;font-weight:800}
.stat span{font-size:11px;line-height:1.3}

/* vouchers */
.vouchers{height:560px;padding-top:30px;text-align:center}
.vouchers h2{font-size:24px;font-weight:800;color:var(--navy);line-height:1.3}
.vouchers h2 em{font-style:normal;color:var(--purple)}
.vouchers .sub{font-size:11px;color:var(--muted);margin-top:4px}
.cards{display:flex;gap:18px;justify-content:center;margin:26px 0 24px}
.card{width:158px;height:270px;border-radius:10px;background:var(--white);box-shadow:0 4px 14px rgba(0,0,0,.12);padding:14px 10px;text-align:left}
.card h3{font-size:16px;font-weight:800;color:var(--navy);line-height:1.1}
.card h3 span{display:block;font-size:12px;font-weight:500;font-style:italic;color:var(--purple)}
.card .art{height:130px;border-radius:6px;margin:12px 0 10px}
.card p{font-size:11px;text-align:center;color:var(--muted)}

/* attract */
.attract{height:320px;display:flex;align-items:center;padding:0 80px;gap:60px}
.attract .copy{width:420px}
.attract h2{font-size:28px;font-weight:800;color:var(--navy)}
.attract h2 em{font-style:normal;color:var(--green)}
.attract p{font-size:13px;margin:10px 0;line-height:1.6}
.attract ul{list-style:none;font-size:13px;line-height:1.6;margin-bottom:10px}
.attract ul li::before{content:"• "}
.attract .photo{width:560px;height:260px;border-radius:14px;background:linear-gradient(180deg,#8ed3ee,#2aa6c4 55%,#1c7c8a)}

/* offers */
.offers{height:680px;background:var(--navy);color:var(--white);text-align:center;padding-top:70px;border-radius:60% 60% 0 0/60px 60px 0 0}
.offers h2{font-size:30px;font-weight:800}
.offers h2 em{font-style:normal;color:#a98bff}
.offers .sub{font-size:14px;margin-top:6px}
.offer-grid{display:grid;grid-template-columns:310px 380px 310px;grid-template-rows:160px 160px;gap:22px;justify-content:center;margin:30px 0 26px}
.offer{border-radius:12px;position:relative;overflow:hidden;display:flex;align-items:flex-end;justify-content:center;padding-bottom:16px}
.offer span{background:rgba(20,16,70,.75);padding:6px 14px;border-radius:8px;font-weight:700;font-size:15px}
.offer-big{grid-row:span 2;background:linear-gradient(180deg,#6fb6d6,#2a6f8e)}
.offer-a{background:linear-gradient(160deg,#c9a78a,#7a5a45)}
.offer-b{background:linear-gradient(160deg,#b993e0,#6a3fb0)}
.offer-c{background:linear-gradient(160deg,#e9c77d,#b07a36)}
.offer-d{background:linear-gradient(160deg,#8fd0e8,#2a7fa8)}

/* ad packs */
.adpacks{height:480px;text-align:center;padding-top:40px;background:linear-gradient(180deg,#ffffff,#f7f4ff)}
.adpacks h2{font-size:30px;font-weight:800;color:var(--navy)}
.adpacks h2 em{font-style:normal;color:var(--violet)}
.adpacks p{font-size:13px;max-width:720px;margin:10px auto 0;line-height:1.5}
.slider{display:flex;align-items:center;justify-content:center;gap:20px;margin:28px 0 24px}
.arrow{width:40px;height:40px;border-radius:50%;background:var(--navy);display:flex;align-items:center;justify-content:center}
.slide{width:220px;height:160px;border-radius:8px;background:var(--white);box-shadow:0 4px 14px rgba(0,0,0,.12);padding:10px}
.slide div{height:100%;border-radius:4px}
.slide.main{width:300px;height:200px}

/* testimonials */
.reviews{height:640px;background:var(--navy);color:var(--white);text-align:center;padding-top:60px}
.reviews h2{font-size:32px;font-weight:800}
.reviews h2 em{font-style:normal;color:#a98bff}
.reviews .sub{font-size:14px;margin-top:6px}
.quotes{display:flex;align-items:center;justify-content:center;gap:20px;margin:40px 0 30px}
.quote{background:var(--white);color:var(--ink);border-radius:12px;padding:60px 20px 20px;position:relative;text-align:left;font-size:11px;line-height:1.55}
.quote.side{width:300px;height:250px;opacity:.9}
.quote.main{width:380px;height:320px}
.avatar{position:absolute;top:-40px;left:50%;transform:translateX(-50%);width:80px;height:80px;border-radius:50%;background:linear-gradient(135deg,#c9b7f5,#6a4fc0);border:4px solid var(--white)}
.quote h4{text-align:center;font-size:15px;color:var(--navy);margin-bottom:8px}

/* closing */
.closing{height:360px;display:flex;align-items:center;padding:0 100px;justify-content:space-between}
.closing .copy{width:560px}
.closing h2{font-size:30px;font-weight:800;color:var(--navy);line-height:1.25}
.closing h2 em{font-style:normal;color:var(--purple)}
.closing p{font-size:14px;margin:12px 0 16px}
.closing .stack{width:380px;height:240px;border-radius:14px;background:linear-gradient(135deg,#f0c35a,#e06a9a 50%,#4fa8d6);transform:rotate(-6deg)}

/* footer */
.footer{height:420px;background:var(--navy-deep);color:var(--white);display:flex;padding:40px 60px;gap:50px;font-size:11px;line-height:1.7}
.footer h5{font-size:14px;font-weight:700;margin-bottom:10px;letter-spacing:.5px}
.f-brand{width:270px}
.f-brand .brand{color:var(--white)}
.f-brand .brand small{color:#b9a8ff}
.socials{display:flex;gap:10px;margin:20px 0}
.socials i{width:30px;height:30px;border-radius:50%;background:#3a3580;display:block}
.f-col{flex:1}
.get{background:var(--green);color:var(--white);border-radius:22px;padding:10px 34px;font-weight:700;font-size:14px;display:inline-block}
.copyright{height:32px;background:#0d0a33;color:#bcbad8;font-size:10px;display:flex;align-items:center;justify-content:space-between;padding:0 60px}
</style>
</head>
<body>

<header>
  <div class="topbar">
    <div class="brand"><span class="brand-dot"></span><div>Brightlane<small>PROMOWORKS</small></div></div>
    <div class="account"><span>Login</span><span>Sign Up</span></div>
  </div>
  <nav class="navbar">
    <span>Home</span><span>Incentives List</span><span>Get Free Samples</span><span>Integrations</span><span>Industries ▾</span>
    <span class="spacer"></span>
    <span class="nav-btn nav-green">Call or Text ▾</span>
    <span class="nav-btn nav-yellow">Book A Demo ▾</span>
  </nav>
</header>

<section class="hero">
  <h1>Increase Your Sales: <em>Give Unlimited Complimentary<br>Bonus Gift Vouchers</em> to Your Customers</h1>
  <p class="lead"><b>Watch Below</b> To See How Your Industry Uses Our Incentives To <b>Skyrocket Their Sales!</b></p>
  <div class="video" role="img" aria-label="Video still of a tropical resort pool with a play button">
    <svg width="64" height="44" viewBox="0 0 64 44"><rect width="64" height="44" rx="10" fill="#e8442d"/><path d="M26 13 L42 22 L26 31Z" fill="#fff"/></svg>
  </div>
  <div class="ctas">
    <a class="btn btn-red">Sign Up For 14 Days Risk Free</a>
    <a class="btn btn-outline">Book A Live Call</a>
  </div>
  <p class="note">*No credit card required*</p>
</section>

<section class="stats">
  <div class="stat"><i class="stat-icon"></i><div><b>16+</b><span>Years In<br>Business</span></div></div>
  <div class="stat"><i class="stat-icon"></i><div><b>17K+</b><span>Clients<br>Enrolled</span></div></div>
  <div class="stat"><i class="stat-icon"></i><div><b>11M+</b><span>Certificates<br>Circulated</span></div></div>
  <div class="stat"><i class="stat-icon"></i><div><b>400K</b><span>Incentives<br>Redeemed</span></div></div>
  <div class="stat"><i class="stat-icon"></i><div><b>$20M+</b><span>In Savings<br>For Redeemers</span></div></div>
  <div class="stat"><i class="stat-icon"></i><div><b>100's</b><span>Of Reviews<br>&amp; Testimonials</span></div></div>
</section>

<section class="vouchers">
  <h2>GIVE AWAY AN <em>UNLIMITED AMOUNT</em> OF COMPLIMENTARY GIFT VOUCHERS<br>TO YOUR CUSTOMERS THAT IS REDEEMABLE FOR:</h2>
  <p class="sub">(without having to personally fulfill or pay for any of them yourself)</p>
  <div class="cards">
    <div class="card"><h3>Hotel Saving<span>Cards</span></h3><div class="art" role="img" aria-label="Hotel savings card artwork" style="background:linear-gradient(160deg,#f2c98a,#b5723e)"></div><p>Complimentary 3 Night Hotel Savings</p></div>
    <div class="card"><h3>Smart Device<span>Certificate</span></h3><div class="art" role="img" aria-label="Smart device certificate artwork" style="background:linear-gradient(160deg,#9fb6e8,#3c4f9a)"></div><p>Complimentary Smart Device</p></div>
    <div class="card"><h3>Restaurant<span>Cards</span></h3><div class="art" role="img" aria-label="Restaurant card artwork" style="background:linear-gradient(160deg,#e9a27a,#9a3b2c)"></div><p>Complimentary $25 Dining Cards</p></div>
    <div class="card"><h3>Airfare<span>Vouchers</span></h3><div class="art" role="img" aria-label="Airfare voucher artwork" style="background:linear-gradient(160deg,#f0b9c8,#b04f7a)"></div><p>Complimentary Roundtrip Airfare</p></div>
    <div class="card"><h3>Cruise<span>Certificates</span></h3><div class="art" role="img" aria-label="Cruise certificate artwork" style="background:linear-gradient(160deg,#a9d9ef,#2a7fae)"></div><p>Complimentary Cruise Getaways</p></div>
    <div class="card"><h3>Resort<span>Certificates</span></h3><div class="art" role="img" aria-label="Resort certificate artwork" style="background:linear-gradient(160deg,#f4c87d,#d0763a)"></div><p>Complimentary All Inclusive Vacations</p></div>
  </div>
  <a class="btn btn-red">Sign Up For 14 Days Risk Free</a>
</section>

<section class="attract">
  <div class="copy">
    <h2><em>Attract</em> New Customers</h2>
    <p>Just by Giving Away Free Vacation Certificates:</p>
    <ul><li>Cruise Vouchers</li><li>Smart Devices</li><li>Dining Takeout Vouchers</li><li>And More</li></ul>
    <p>You'll <b>Never Pay</b> For A Single Certificate, Vacation or Any Item Ever.</p>
    <a class="btn btn-outline">Sign Up For 14 Days Risk Free</a>
    <p class="note">*No credit card required*</p>
  </div>
  <div class="photo" role="img" aria-label="Overwater bungalows on a turquoise lagoon"></div>
</section>

<section class="offers">
  <h2>BPW <em>Exclusive</em> Offers</h2>
  <p class="sub">Our Marketing Incentives Can Help You With:</p>
  <div class="offer-grid">
    <div class="offer offer-a" role="img" aria-label="Hotel room welcome scene"><span>Welcome Gifts</span></div>
    <div class="offer offer-big" role="img" aria-label="Beach resort giveaway scene" style="grid-row:1/3;grid-column:2"><span>Special Promotion Giveaway</span></div>
    <div class="offer offer-b" role="img" aria-label="Gift box referral scene"><span>Referral Gifts</span></div>
    <div class="offer offer-c" role="img" aria-label="Airplane window view"><span>Enticement for Booking a Flight</span></div>
    <div class="offer offer-d" role="img" aria-label="Cruise ship at sea"><span>Gifts for Booking a Cruise</span></div>
  </div>
  <a class="btn btn-red">Sign Up For 14 Days Risk Free</a>
</section>

<section class="adpacks">
  <h2><em>Plug-In-Play</em> Ad Packs</h2>
  <p>Proven Friendline® Ad Templates, High Converting Banner Ad Templates To Use With The Searchly® Display Network Plus Timer Tested Print Ad Templates That We Provide To You For Free With Your BPW Package.</p>
  <div class="slider">
    <span class="arrow"><svg width="14" height="14" viewBox="0 0 14 14"><path d="M9 2 L4 7 L9 12" stroke="#fff" stroke-width="2.5" fill="none"/></svg></span>
    <div class="slide"><div role="img" aria-label="Ad template preview" style="background:linear-gradient(135deg,#f7d27a,#e38a3c)"></div></div>
    <div class="slide main"><div role="img" aria-label="Free smart fitness watch ad template" style="background:linear-gradient(135deg,#7ac7e8,#3b5fb8)"></div></div>
    <div class="slide"><div role="img" aria-label="Ad template preview" style="background:linear-gradient(135deg,#b7e3c4,#3e9a6a)"></div></div>
    <span class="arrow"><svg width="14" height="14" viewBox="0 0 14 14"><path d="M5 2 L10 7 L5 12" stroke="#fff" stroke-width="2.5" fill="none"/></svg></span>
  </div>
  <a class="btn btn-red">Sign Up For 14 Days Risk Free</a>
</section>

<section class="reviews">
  <h2>What <em>Our Clients</em> Say...</h2>
  <p class="sub">Here's are others getting their success with our incentives.</p>
  <div class="quotes">
    <div class="quote side"><i class="avatar" role="img" aria-label="Client portrait"></i><h4>Marcus L.</h4><p>We started offering the cruise vouchers to every new booking and our repeat clients doubled within a few months. Setup was quick, the templates saved us hours and our customers genuinely love the bonus gifts they receive.</p></div>
    <div class="quote main"><i class="avatar" role="img" aria-label="Client portrait"></i><h4>Danny R.</h4><p>"Brightlane has been a real partner for our agency. Adding complimentary hotel and resort certificates to our packages gave clients one more reason to book with us instead of online sites. Our closing rate went up, referrals grew and the support team answered every question fast. I recommend it to any travel advisor who wants to stand out."</p></div>
    <div class="quote side"><i class="avatar" role="img" aria-label="Client portrait"></i><h4>Laura P.</h4><p>The dining cards have become our favorite thank you gift. Clients mention them on every return trip and they tell friends about us. It costs us nothing per certificate and it keeps our name top of mind.</p></div>
  </div>
  <a class="btn btn-red">Sign Up For 14 Days Risk Free</a>
</section>

<section class="closing">
  <div class="copy">
    <h2>Increase Your Sales Now With Our <em>COMPLIMENTARY GIFT VOUCHERS</em></h2>
    <p>Imagine Being Able To <b>Offer $1000 Deals</b> With Every Booking!</p>
    <a class="btn btn-red">Sign Up For 14 Days Risk Free</a>
  </div>
  <div class="stack" role="img" aria-label="Fanned stack of gift voucher certificates"></div>
</section>

<footer>
  <div class="footer">
    <div class="f-brand">
      <div class="brand"><span class="brand-dot"></span><div>Brightlane<small>PROMOWORKS</small></div></div>
      <div class="socials"><i></i><i></i><i></i><i></i></div>
      <span class="get">Get Started</span>
    </div>
    <div class="f-col">
      <h5>CONTACT US</h5>
      <p><b>Brightlane Promoworks Group, Inc.</b><br>2840 Harbor Point Way<br>Lakeview Springs, CA 90210</p>
      <p><b>Book A Demo</b><br>Sales: (555) 014-2290<br>Current/New Clients: (555) 014-3381</p>
      <p><b>Call Or Text Us</b><br>support@brightlanepromoworks.biz<br>www.brightlanepromoworks.biz</p>
      <p><b>Hours</b><br>Monday – Friday 9am – 5pm PST<br>*After hours all inquiries answered next day</p>
    </div>
    <div class="f-col">
      <h5>QUICK LINKS</h5>
      <p>Home<br>Incentives List<br>Login<br>Sign Up<br>Affiliates<br>Integrations<br>Testimonials<br>Frequently Asked Questions<br>BPW Brochure<br>Demo Videos<br>White Label Agency Program</p>
    </div>
    <div class="f-col">
      <h5>OTHER LINKS</h5>
      <p>Industries<br>Lead Generation<br>How To Use Certificates<br>Pop Up &amp; Sticky Bars<br>Whitepaper – Incentive Sales<br>Whitepaper – Improve Sales<br>Strategy Sheet<br>Whitepaper – Boost Retention<br>Guarantee</p>
    </div>
  </div>
  <div class="copyright"><span>© 2024 Brightlane Promoworks Group, Inc. All Rights Reserved.</span><span>Privacy Policy · Terms and Conditions</span></div>
</footer>

</body>
</html>
```